Flyer needed for a Summer Course

We need a flyer made for a summer course that will review a chapter of the Qur'an (holy book). The flyer can include imagery related to a table spread with delicious food outdoors in a garden setting, or any generic light/path to a garden or to light. Please include the attached logo to the flyer as well. The following information should be included in the flyer:
Tafsir of Surah Maidah
Taught by Delina Varosh
June 1 to June 15 2017
Daily Monday thru Thursday
1:30 PM to 2:30 PM
Community Hall of Brantwell Township
2470 Kettering Row
Piscataway NJ 07391
For more information: lumenfold7@mailvane.example

```html
<!DOCTYPE html>
<html lang="en">
<head>
<meta charset="utf-8">
<title>Tafsir of Surah Maidah – Summer Course Flyer</title>
<link rel="stylesheet" href="https://fonts.googleapis.com/css2?family=Bodoni+Moda:wght@400;500&family=Roboto+Condensed:wght@700&family=Arimo:wght@400;700&display=swap">
<style>
  :root {
    --sky-deep: #2f7fd0;
    --sky-mid: #5aa6e6;
    --sky-light: #cfe6fa;
    --sun: #ffffff;
    --title-white: #ffffff;
    --accent-red: #e3262b;
    --navy: #2b3a8f;
    --navy-dark: #232f7a;
    --logo-orange: #f08a1c;
    --calligraphy-tint: rgba(120, 215, 235, 0.55);
    --hands-tone: #f1c9b2;
  }
  * { margin: 0; padding: 0; box-sizing: border-box; }
  html, body { width: 849px; height: 1200px; overflow: hidden; background: #ffffff; }
  .flyer {
    position: relative;
    width: 849px;
    height: 1200px;
    overflow: hidden;
    background:
      radial-gradient(circle at 140px 150px, var(--sun) 0, rgba(255,255,255,0.95) 60px, rgba(255,255,255,0.45) 170px, rgba(255,255,255,0) 360px),
      linear-gradient(180deg, var(--sky-deep) 0%, var(--sky-mid) 45%, var(--sky-light) 78%, #ffffff 100%);
    font-family: "Arimo", Arial, sans-serif;
  }
  .calligraphy-art {
    position: absolute;
    left: 250px; top: 250px;
    width: 470px; height: 320px;
    border-radius: 50%;
    background: radial-gradient(ellipse at center, var(--calligraphy-tint) 0%, rgba(120,215,235,0.25) 55%, rgba(120,215,235,0) 75%);
  }
  .hands-photo {
    position: absolute;
    left: 90px; top: 520px;
    width: 660px; height: 490px;
    background: radial-gradient(ellipse 55% 50% at 50% 42%, var(--hands-tone) 0%, rgba(241,201,178,0.75) 45%, rgba(255,255,255,0.55) 75%, rgba(255,255,255,0) 100%);
  }
  .title {
    position: absolute;
    color: var(--title-white);
    font-family: "Bodoni Moda", "Didot", serif;
    font-weight: 400;
    line-height: 1;
  }
  .title-tafsir { left: 52px; top: 12px; font-size: 176px; letter-spacing: 2px; }
  .title-of { left: 228px; top: 180px; font-size: 230px; letter-spacing: -6px; }
  .title-surah { left: 494px; top: 250px; font-size: 68px; line-height: 58px; }
  .teacher-bar {
    position: absolute;
    left: 498px; top: 388px;
    width: 351px; height: 34px;
    background: #ffffff;
    padding-left: 10px;
    color: var(--accent-red);
    font-family: "Bodoni Moda", serif;
    font-weight: 500;
    font-size: 21px;
    line-height: 34px;
  }
  .schedule {
    position: absolute;
    left: 56px; top: 884px;
    color: var(--accent-red);
    font-family: "Roboto Condensed", "Arial Narrow", sans-serif;
    font-weight: 700;
    font-size: 25px;
    line-height: 34px;
  }
  .skyline {
    position: absolute;
    left: 0; top: 1010px;
    width: 849px; height: 190px;
  }
  .footer-band {
    position: absolute;
    left: 0; top: 1080px;
    width: 849px; height: 120px;
    background: var(--navy);
  }
  .venue {
    position: absolute;
    left: 56px; top: 1104px;
    color: #ffffff;
    font-size: 14px;
    line-height: 20px;
  }
  .venue strong { font-weight: 700; }
  .institute-mark {
    position: absolute;
    left: 556px; top: 1120px;
    display: flex;
    align-items: center;
    gap: 10px;
    color: var(--logo-orange);
    font-family: "Roboto Condensed", "Arial Narrow", sans-serif;
    font-weight: 700;
    font-size: 26px;
  }
  .institute-dot {
    width: 20px; height: 20px;
    border-radius: 50%;
    background: var(--logo-orange);
  }
</style>
</head>
<body>
  <main class="flyer">
    <div class="calligraphy-art" role="img" aria-label="Faint turquoise Arabic calligraphy floating in the sky"></div>
    <div class="hands-photo" role="img" aria-label="Photograph of open hands raised together in prayer"></div>

    <h1>
      <span class="title title-tafsir">Tafsir</span>
      <span class="title title-of">Of</span>
      <span class="title title-surah">Surah<br>Maidah</span>
    </h1>
    <p class="teacher-bar">Taught by Delina Varosh</p>

    <p class="schedule">June 1 to June 15 2017<br>Daily Monday thru Thursday<br>1:30 PM to 2:30 PM</p>

    <svg class="skyline" viewBox="0 0 849 190" role="img" aria-label="Navy silhouette of a mosque skyline with domes and minarets">
      <rect x="0" y="40" width="849" height="150" fill="var(--navy-dark)"/>
    </svg>
    <div class="footer-band"></div>

    <address class="venue">
      <strong>Community Hall of Brantwell Township</strong><br>
      2470 Kettering Row | Piscataway NJ 07391<br>
      <strong>For more information:</strong> lumenfold7@mailvane.example
    </address>

    <div class="institute-mark">
      <span class="institute-dot"></span>
      <span>Lanterhall Institute</span>
    </div>
  </main>
</body>
</html>
```